依頼概要
■依頼の目的/概要
弊社ではあささんぽ、あさひを浴びようと思えるSNSアプリの制作を行っております。
そよかぜてちょうアプリでは毎日の記録をつけるためのライフログ系の機能を制作しております。

ライフログとして自分の記録を見返したり、他のユーザーからも見てもらえる機能がある日記のデザイン及びその画面のUI制作をお願いします。

■依頼の詳細
ユーザーが投稿するのは朝日を含めた毎朝の日記で自分のそよかぜてちょう(本のテイスト)の左ページを投稿します(アプリ上ホーム画面)。その日記投稿や朝散歩をすればするほど幸せの証として「そよかぜスター」を報酬として獲得し、毎朝獲得したハートを自分のそよかぜてちょうの右ページに貯めておけます(アプリ上そよかぜてちょう画面)。

今回トライアルでお願いしたいのはユーザーが朝日を投稿するホーム画面のUIです(左ページ)。
必要な要項といたしましては、
・ユーザーが撮影した朝日の写真(必須)
・日付(必須)
・天気※
・場所※
・気温※
・日記コメント※
・自分のキャラクター(こちらは素材があります)※

を入れられるようにしたいと考えております。
※は、ユーザー任意で入れたり、非表示にできます

スワイプすると、他のユーザーの日記のページをめくるような感覚のモーションの検討もしています。

こちらをトライアルという形で、採用された方には別画面/別バージョンの本のデザインや詳細なUIなどご相談したいと考えております。追加のUIのお見積りなども含め、ご提案いただけますと幸いです。

現在の開発中の仮デザインを添付しますが、よりよいデザインを是非、応募いただけますと幸いです。

画面UIのデザインがイメージと合っていた為。

この度、ご提案いただきありがとうございました。ご厚情にお応えすることができず、誠に申し訳ございません。勝手ではございますが、これに懲りず今後ともお付き合いくださいますようお願い申し上げます。

```html
<!DOCTYPE html>
<html lang="ja">
<head>
<meta charset="utf-8">
<title>ホーム</title>
<link rel="stylesheet" href="https://fonts.googleapis.com/css2?family=Noto+Sans+JP:wght@400;500;700&display=swap">
<style>
  :root {
    --bar-bg: #f8ede8;
    --page-bg: #fffbf9;
    --paper: #fffdf8;
    --paper-edge: #efe3da;
    --rule: #f1e4da;
    --spine: #f3c9b8;
    --ink: #1f1b19;
    --muted: #4a413d;
    --sun: #fdb813;
    --accent: #fdd9cc;
    --pill: #fcd8c9;
    --dawn-top: #f6b48f;
    --dawn-mid: #fbd3a4;
    --dawn-low: #c9a9b8;
    --chara: #f6e2d6;
  }
  * { box-sizing: border-box; margin: 0; padding: 0; }
  html, body { width: 677px; height: 1200px; overflow: hidden; }
  body {
    font-family: "Noto Sans JP", sans-serif;
    background: var(--page-bg);
    color: var(--ink);
    position: relative;
  }
  .app-bar {
    position: absolute; top: 0; left: 0; right: 0; height: 138px;
    background: var(--bar-bg);
    display: flex; align-items: center; justify-content: space-between;
    padding: 0 30px 0 36px;
  }
  .app-bar__title { font-size: 38px; font-weight: 400; letter-spacing: 1px; }
  .icon-btn { width: 50px; height: 50px; display: flex; align-items: center; justify-content: center; }

  .diary-page {
    position: absolute; left: 32px; right: 32px; top: 166px; height: 650px;
    background: var(--paper);
    border: 1px solid var(--paper-edge);
    border-left: 10px solid var(--spine);
    border-radius: 6px 18px 18px 6px;
    box-shadow: 0 6px 16px rgba(120, 80, 60, 0.12);
    padding: 28px 28px 28px 24px;
  }
  .sunrise-photo {
    height: 250px; border-radius: 12px;
    background: linear-gradient(180deg, var(--dawn-top) 0%, var(--dawn-mid) 55%, var(--dawn-low) 100%);
  }
  .diary-meta {
    margin-top: 20px; height: 44px;
    display: flex; align-items: center; gap: 14px;
    font-size: 26px; font-weight: 500;
  }
  .diary-meta__item { display: flex; align-items: center; gap: 8px; }
  .diary-meta__sep { width: 1px; height: 26px; background: var(--paper-edge); }
  .diary-body {
    margin-top: 16px; position: relative; height: 264px;
    background: repeating-linear-gradient(180deg, transparent 0 43px, var(--rule) 43px 44px);
  }
  .diary-comment { font-size: 26px; line-height: 44px; font-weight: 400; }
  .diary-comment strong { font-weight: 700; }
  .diary-comment p + p { margin-top: 44px; }
  .diary-character {
    position: absolute; right: 0; bottom: 8px; width: 100px; height: 100px;
    border-radius: 50%; background: var(--chara);
  }

  .fab {
    position: absolute; left: 524px; top: 876px; width: 117px; height: 117px;
    border-radius: 30px; background: var(--accent);
    box-shadow: 0 4px 10px rgba(0,0,0,0.18);
    display: flex; align-items: center; justify-content: center;
  }
  .bottom-nav {
    position: absolute; left: 0; right: 0; bottom: 0; height: 169px;
    background: var(--bar-bg);
    display: flex; justify-content: space-around; align-items: flex-start;
    padding-top: 24px;
  }
  .nav-item {
    width: 200px; display: flex; flex-direction: column; align-items: center;
    font-size: 22px; font-weight: 500; color: var(--muted);
  }
  .nav-item__icon {
    width: 135px; height: 68px; border-radius: 34px;
    display: flex; align-items: center; justify-content: center;
    margin-bottom: 14px;
  }
  .nav-item--active .nav-item__icon { background: var(--pill); }
  .nav-item--active { color: var(--ink); }
</style>
</head>
<body>
  <header class="app-bar">
    <div class="icon-btn" aria-label="メニュー">
      <svg width="36" height="28" viewBox="0 0 36 28"><g fill="#2a2422"><rect y="1" width="36" height="4"/><rect y="12" width="36" height="4"/><rect y="23" width="36" height="4"/></g></svg>
    </div>
    <h1 class="app-bar__title">2023年3月12日</h1>
    <div class="icon-btn" aria-label="アカウント">
      <svg width="46" height="46" viewBox="0 0 24 24"><path fill="#2a2422" d="M12 2a10 10 0 1 0 0 20 10 10 0 0 0 0-20zm0 3.2a3.3 3.3 0 1 1 0 6.6 3.3 3.3 0 0 1 0-6.6zM12 19.4a7.6 7.6 0 0 1-5.9-2.9c.6-1.8 3.4-2.9 5.9-2.9s5.3 1.1 5.9 2.9a7.6 7.6 0 0 1-5.9 2.9z"/></svg>
    </div>
  </header>

  <article class="diary-page">
    <div class="sunrise-photo" role="img" aria-label="ユーザーが撮影した朝日の写真"></div>

    <div class="diary-meta">
      <span class="diary-meta__item">
        <svg width="36" height="36" viewBox="0 0 100 100" aria-hidden="true">
          <circle cx="50" cy="50" r="24" fill="var(--sun)"/>
          <g stroke="var(--sun)" stroke-width="8" stroke-linecap="round">
            <line x1="50" y1="4" x2="50" y2="14"/><line x1="50" y1="86" x2="50" y2="96"/>
            <line x1="4" y1="50" x2="14" y2="50"/><line x1="86" y1="50" x2="96" y2="50"/>
            <line x1="17.5" y1="17.5" x2="24.5" y2="24.5"/><line x1="75.5" y1="75.5" x2="82.5" y2="82.5"/>
            <line x1="17.5" y1="82.5" x2="24.5" y2="75.5"/><line x1="75.5" y1="24.5" x2="82.5" y2="17.5"/>
          </g>
        </svg>晴れ
      </span>
      <span class="diary-meta__sep"></span>
      <span class="diary-meta__item">11℃</span>
      <span class="diary-meta__sep"></span>
      <span class="diary-meta__item">
        <svg width="26" height="30" viewBox="0 0 24 28" aria-hidden="true"><path fill="#2a2422" d="M12 1a9 9 0 0 0-9 9c0 6.5 9 17 9 17s9-10.5 9-17a9 9 0 0 0-9-9zm0 12.4a3.4 3.4 0 1 1 0-6.8 3.4 3.4 0 0 1 0 6.8z"/></svg>東京都
      </span>
    </div>

    <div class="diary-body">
      <div class="diary-comment">
        <p>おはようございます！<br>今日の東京都の天気は<strong>晴れ</strong>、<br>気温は<strong>11℃</strong>です。</p>
        <p>お気に入りのパーカーを羽織って、<br>朝日を浴びに行きましょう！</p>
      </div>
      <div class="diary-character" role="img" aria-label="自分のキャラクター"></div>
    </div>
  </article>

  <div class="fab" aria-label="日記を書く">
    <svg width="40" height="40" viewBox="0 0 24 24"><path fill="#2a2422" d="M3 17.25V21h3.75L17.8 9.94l-3.75-3.75L3 17.25zm2.92 2.33H5v-.92l9.06-9.06.92.92L5.92 19.58zM20.7 7.04a1 1 0 0 0 0-1.41l-2.34-2.34a1 1 0 0 0-1.41 0l-1.830 1.83 3.75 3.75 1.83-1.83z"/></svg>
  </div>

  <nav class="bottom-nav">
    <div class="nav-item nav-item--active">
      <div class="nav-item__icon">
        <svg width="38" height="38" viewBox="0 0 24 24"><path fill="#2a2422" d="M4 21V10l8-6 8 6v11h-6v-6h-4v6z"/></svg>
      </div>ホーム
    </div>
    <div class="nav-item">
      <div class="nav-item__icon">
        <svg width="48" height="40" viewBox="0 0 28 24"><g fill="none" stroke="#2a2422" stroke-width="2"><circle cx="14" cy="8" r="3.5"/><circle cx="6" cy="10" r="2.6"/><circle cx="22" cy="10" r="2.6"/><path d="M8 20v-1.5c0-2.5 3-4 6-4s6 1.5 6 4V20z"/><path d="M2 20v-1c0-1.8 1.7-3 4-3M26 20v-1c0-1.8-1.7-3-4-3"/></g></svg>
      </div>みんなの投稿
    </div>
    <div class="nav-item">
      <div class="nav-item__icon">
        <svg width="38" height="38" viewBox="0 0 24 24"><path fill="#2a2422" d="M19 4h-1V2h-2v2H8V2H6v2H5a2 2 0 0 0-2 2v14a2 2 0 0 0 2 2h8v-2H5V10h14v3h2V6a2 2 0 0 0-2-2zM7 12h4v4H7zm9 3l-3 3v3h3l3-3-3-3zm2.5-.5l3 3 1-1-3-3z"/></svg>
      </div>記録
    </div>
  </nav>
</body>
</html>
```